1923 Basins & Spouts Business Card

I'm wanting to get a business card designed. Our business is 1923 Basins & Spouts
Details for the card:

1923 Basins & Spouts
Name: Gareth Vostle
Email: gareth@1923basinsandspouts.com.au
Website: www.1923basinsandspouts.com.au
Mobile: 0439 602 158
Phone: 02 5550 1843

Font of Basins & Spouts is called Snell Roundhand. Not sue what font logo text is.

I'm thinking two sided but it doesn't have to be.

```html
<!DOCTYPE html>
<html lang="en">
<head>
<meta charset="utf-8">
<title>1923 Basins &amp; Spouts — Business Card</title>
<link rel="stylesheet" href="https://fonts.googleapis.com/css2?family=Tinos:wght@400;700&family=Lato:wght@400&display=swap">
<style>
  :root {
    --backdrop: #dcdcdc;
    --card-white: #ffffff;
    --band-dark: #2f2f2f;
    --band-pattern: #3a3a3a;
    --ink: #111111;
    --ink-soft: #333333;
    --on-dark: #f2f2f2;
    --on-dark-soft: #c9c9c9;
  }
  * { box-sizing: border-box; margin: 0; padding: 0; }
  html, body {
    width: 1200px; height: 864px; overflow: hidden;
    background: var(--backdrop);
  }
  .sheet {
    width: 1200px; height: 864px;
    display: flex; align-items: center; justify-content: center; gap: 40px;
  }
  .card {
    position: relative;
    width: 540px; height: 310px;
    background: var(--card-white);
    box-shadow: 0 6px 18px rgba(0,0,0,0.18);
    overflow: hidden;
  }
  .band {
    position: absolute; left: 0; right: 0;
    background: radial-gradient(circle at 20% 50%, var(--band-pattern), var(--band-dark) 60%);
  }
  .card--brand .band { top: 124px; bottom: 0; }
  .card--contact .band { top: 0; height: 142px; }

  .brand {
    position: absolute;
    display: flex; align-items: center; gap: 14px;
  }
  .brand__mark {
    width: 64px; height: 64px; border-radius: 50%;
    border: 2px solid currentColor;
    flex: none;
  }
  .brand__name {
    font-family: "Tinos", "Times New Roman", serif;
    font-weight: 400; font-size: 30px; letter-spacing: 0.5px;
    white-space: nowrap;
  }
  .tagline {
    position: absolute;
    font-family: "Lato", Arial, sans-serif;
    font-size: 11px; letter-spacing: 0.2px;
    white-space: nowrap;
  }

  .card--brand .brand { left: 50px; top: 26px; color: var(--ink); }
  .card--brand .tagline { left: 128px; top: 94px; color: var(--ink-soft); }

  .card--contact .brand { left: 30px; top: 28px; color: var(--on-dark); }
  .card--contact .tagline { left: 108px; top: 98px; color: var(--on-dark-soft); }

  .person {
    position: absolute; left: 0; right: 0; top: 162px;
    text-align: center;
    font-family: "Tinos", "Times New Roman", serif;
    color: var(--ink);
  }
  .person__name { font-weight: 700; font-size: 24px; margin-bottom: 10px; }
  .contact-list { list-style: none; font-size: 14px; line-height: 18px; }
</style>
</head>
<body>
<main class="sheet">

  <section class="card card--brand">
    <div class="band" role="img" aria-label="Dark band with a faint repeating ornamental frame pattern"></div>
    <div class="brand">
      <span class="brand__mark"></span>
      <span class="brand__name">1923 Basins &amp; Spouts</span>
    </div>
    <p class="tagline">Pairing classic elegance with everyday usefulness</p>
  </section>

  <section class="card card--contact">
    <div class="band" role="img" aria-label="Dark band with a faint repeating ornamental frame pattern"></div>
    <div class="brand">
      <span class="brand__mark"></span>
      <span class="brand__name">1923 Basins &amp; Spouts</span>
    </div>
    <p class="tagline">Pairing classic elegance with everyday usefulness</p>
    <div class="person">
      <h1 class="person__name">Gareth Vostle</h1>
      <ul class="contact-list">
        <li>0439 602 158</li>
        <li>02 5550 1843</li>
        <li>gareth@1923basinsandspouts.com.au</li>
        <li>www.1923basinsandspouts.com.au</li>
      </ul>
    </div>
  </section>

</main>
</body>
</html>
```